Bauunternehmen sucht originellen Gerüst-Banner
Zielgruppe
Bauunternehmen mit Schwerpunkt Gerüstbau.
Aufgabenstellung
Wir suchen einen neu designten Gerüst-Banner, der zukünftig an unseren Baustellen hängen soll.
Der Banner sollte den Namen (Dorne + Felsing GmbH), das Logo (siehe Anhang!) und die Website (dorne-felsing.de) beinhalten. Ansonsten haben die Designer freie Hand. Verspielte Designs (gerne auch mit Comic-Figur) sind ebenso erwünscht wie schnörkellose klassische Designs. Es sollte lediglich berücksichtigt werden, dass der Banner später 2,50 m breit und 2,00 m hoch sein wird.

```html
<!DOCTYPE html>
<html lang="de">
<head>
<meta charset="utf-8">
<title>Gerüst-Banner Dorne + Felsing GmbH</title>
<link rel="stylesheet" href="https://fonts.googleapis.com/css2?family=Open+Sans:ital,wdth,wght@0,75..100,400..800;1,75..100,400..800&display=swap">
<style>
  :root {
    --brand-red: #c0202b;
    --white: #ffffff;
    --page-bg: #e9e9e9;
    --sky-light: #c9cbc6;
    --sky-mid: #8c9196;
    --sky-dark: #4d5560;
    --haze: #a7a99f;
    --city: #6e716c;
    --cape-red: #b8322c;
    --cape-dark: #8e241f;
    --brick: #5a4640;
    --brick-dark: #3b2f2c;
  }
  * { margin: 0; padding: 0; box-sizing: border-box; }
  html, body {
    width: 1200px;
    height: 1200px;
    overflow: hidden;
    background: var(--page-bg);
    font-family: "Open Sans", Arial, sans-serif;
  }
  .banner {
    position: absolute;
    left: 50px;
    top: 160px;
    width: 1100px;
    height: 880px;
    overflow: hidden;
    box-shadow: 0 6px 24px rgba(0,0,0,0.18);
  }
  .backdrop-photo {
    position: absolute;
    inset: 0;
    background:
      radial-gradient(ellipse at 60% 35%, rgba(230,230,220,0.55), transparent 55%),
      linear-gradient(180deg, var(--sky-dark) 0%, var(--sky-mid) 28%, var(--sky-light) 52%, var(--haze) 70%, var(--city) 100%);
  }
  .hero-photo {
    position: absolute;
    left: 600px;
    top: 170px;
    right: 0;
    bottom: 0;
    border-radius: 120px 0 0 0;
    background:
      radial-gradient(ellipse at 25% 20%, rgba(120,150,190,0.55), transparent 30%),
      linear-gradient(180deg, var(--cape-red) 0%, var(--cape-dark) 55%, var(--brick) 75%, var(--brick-dark) 100%);
  }
  .headline {
    position: absolute;
    left: 70px;
    top: 150px;
    transform: rotate(-5deg);
    transform-origin: left top;
    display: flex;
    flex-direction: column;
    gap: 10px;
  }
  .headline-line {
    align-self: flex-start;
    background: var(--brand-red);
    color: var(--white);
    font-weight: 700;
    font-stretch: 87.5%;
    font-size: 62px;
    line-height: 1;
    text-transform: uppercase;
    letter-spacing: 0.5px;
    padding: 8px 22px 10px 34px;
  }
  .brand-mark {
    position: absolute;
    right: 50px;
    top: 50px;
    width: 170px;
    height: 160px;
    background: var(--brand-red);
    display: flex;
    align-items: flex-end;
    justify-content: center;
    padding-bottom: 16px;
  }
  .brand-name {
    color: var(--white);
    font-weight: 700;
    font-stretch: 87.5%;
    font-size: 24px;
    text-align: center;
    line-height: 1.1;
  }
  .company-name {
    position: absolute;
    left: 78px;
    bottom: 142px;
    color: var(--white);
    font-weight: 600;
    font-stretch: 87.5%;
    font-size: 36px;
  }
  .url-band {
    position: absolute;
    left: 0;
    right: 0;
    bottom: 40px;
    height: 86px;
    background: var(--white);
    display: flex;
    align-items: center;
    padding-left: 70px;
  }
  .url {
    color: var(--brand-red);
    font-weight: 700;
    font-style: italic;
    font-stretch: 87.5%;
    font-size: 54px;
  }
</style>
</head>
<body>
  <div class="banner">
    <div class="backdrop-photo" role="img" aria-label="Foto: dunstige Großstadtskyline unter bewölktem Himmel"></div>
    <div class="hero-photo" role="img" aria-label="Foto: Kind mit blauer Maske und rotem Umhang sitzt nachdenklich auf einem Backsteinschornstein"></div>

    <div class="brand-mark">
      <span class="brand-name">Dorne +<br>Felsing</span>
    </div>

    <div class="headline">
      <span class="headline-line">Irgendwie</span>
      <span class="headline-line">müssen Sie ja</span>
      <span class="headline-line">aufs Dach</span>
      <span class="headline-line">kommen.</span>
    </div>

    <p class="company-name">Dorne + Felsing GmbH</p>

    <div class="url-band">
      <span class="url">www.dorne-felsing.de</span>
    </div>
  </div>
</body>
</html>
```